Icon set for a restaurant and travel guide

Please visit tovami.com to get more info about our site. We have attached a pdf for more detailed info.

Target Market(s)

Restaurant and travel lovers

Industry/Entity Type

Restaurant

```html
<!DOCTYPE html>
<html lang="en">
<head>
<meta charset="utf-8">
<title>Tovami guide icon menu</title>
<link rel="stylesheet" href="https://fonts.googleapis.com/css2?family=Jost:wght@400;500&display=swap">
<style>
  :root {
    --bg-top: #ddcd74;
    --bg-bottom: #fcf8dd;
    --ink: #151515;
    --tile-top: #fbfbf9;
    --tile-bottom: #c9dde7;
    --icon-dark: #2b2b2b;
    --icon-grey: #8a8a8a;
    --star: #e0c21c;
    --target: #c8141e;
    --globe-sea: #2a9bd6;
    --globe-land: #1f7a3b;
    --paper: #f1ead0;
    --chair: #7a1a2a;
    --primary: #be1622;
    --primary-text: #ffffff;
    --secondary: #d3eaf8;
    --secondary-text: #7592a4;
    --secondary-arrow: #2b2b2b;
  }
  * { margin: 0; padding: 0; box-sizing: border-box; }
  html, body { width: 1200px; height: 900px; overflow: hidden; }
  body {
    position: relative;
    background: linear-gradient(to bottom, var(--bg-top), var(--bg-bottom));
    font-family: "Jost", "Futura", sans-serif;
  }
  .menu-item { position: absolute; width: 200px; margin-left: -100px; text-align: center; }
  .menu-item__label {
    font-size: 20px; font-weight: 500; color: var(--ink);
    font-variant: small-caps; text-transform: lowercase; letter-spacing: .5px;
    height: 40px; line-height: 40px; white-space: nowrap;
  }
  .menu-item__label::first-letter { text-transform: uppercase; }
  .tile {
    width: 122px; height: 120px; margin: 0 auto; border-radius: 8px;
    background: linear-gradient(to bottom, var(--tile-top) 55%, var(--tile-bottom));
    box-shadow: 0 1px 2px rgba(0,0,0,.15);
    display: flex; align-items: center; justify-content: center;
    position: relative;
  }
  .tile::after {
    content: ""; position: absolute; left: 0; right: 0; top: 124px; height: 24px;
    border-radius: 8px 8px 0 0;
    background: linear-gradient(to bottom, rgba(150,130,60,.28), rgba(150,130,60,0));
  }
  .tile svg { width: 96px; height: 96px; }
  .icon-fill { width: 90px; height: 90px; border-radius: 10px; }
  .icon-fill--hands { background: linear-gradient(90deg, #9a9a9a, #3a3a3a); height: 40px; }
  .icon-fill--globe { border-radius: 50%; background: radial-gradient(circle at 45% 45%, var(--globe-land) 0 30%, var(--globe-sea) 32%); width: 82px; height: 82px; }
  .icon-fill--papers { background: linear-gradient(135deg, var(--paper), #d8d0b4); width: 84px; height: 96px; border-radius: 2px; }
  .icon-fill--chair { background: linear-gradient(to bottom, #3a0612, var(--chair)); width: 88px; height: 78px; border-radius: 6px; }

  .action {
    position: absolute; left: 382px; width: 457px;
    display: flex; align-items: center; padding-left: 20px;
    font-variant: small-caps; text-transform: lowercase; font-weight: 400;
    letter-spacing: 1px;
  }
  .action__arrow { width: 0; height: 0; border-top: 12px solid transparent; border-bottom: 12px solid transparent; border-left: 20px solid; margin-right: 22px; }
  .action--primary { top: 632px; height: 78px; background: var(--primary); color: var(--primary-text); font-size: 62px; }
  .action--primary .action__arrow { border-left-color: var(--primary-text); }
  .action--secondary { top: 752px; height: 77px; background: var(--secondary); color: var(--secondary-text); font-size: 62px; }
  .action--secondary .action__arrow { border-left-color: var(--secondary-arrow); }
  .action__text::first-letter { text-transform: uppercase; }
</style>
</head>
<body>
  <nav class="icon-menu">
    <div class="menu-item" style="left:192px; top:88px">
      <div class="menu-item__label">Affiliation</div>
      <div class="tile" style="margin-top:23px"><div class="icon-fill icon-fill--hands" role="img" aria-label="Handshake icon"></div></div>
    </div>
    <div class="menu-item" style="left:380px; top:95px">
      <div class="menu-item__label">Events</div>
      <div class="tile" style="margin-top:17px">
        <svg viewBox="0 0 96 96" aria-label="Music notes">
          <g fill="var(--icon-dark)">
            <rect x="10" y="6" width="4" height="78"/><rect x="10" y="6" width="30" height="4"/>
            <rect x="36" y="6" width="4" height="28"/><circle cx="13" cy="84" r="8"/><circle cx="44" cy="34" r="8"/>
            <rect x="40" y="50" width="4" height="36"/><rect x="40" y="50" width="42" height="4"/>
            <rect x="78" y="50" width="4" height="24"/><circle cx="44" cy="86" r="8"/><circle cx="84" cy="76" r="8"/>
          </g>
        </svg>
      </div>
    </div>
    <div class="menu-item" style="left:580px; top:95px">
      <div class="menu-item__label">Consumer service</div>
      <div class="tile" style="margin-top:17px">
        <svg viewBox="0 0 96 96" aria-label="Telephone">
          <path d="M40 8 L30 12 C20 30 20 62 34 82 L44 88 L52 78 L42 68 C36 56 36 40 42 28 L50 20 Z" fill="var(--icon-dark)"/>
          <path d="M44 70 L62 88 M50 64 L68 84" stroke="var(--icon-dark)" stroke-width="4"/>
        </svg>
      </div>
    </div>
    <div class="menu-item" style="left:790px; top:95px">
      <div class="menu-item__label">Popular destination</div>
      <div class="tile" style="margin-top:17px">
        <svg viewBox="0 0 96 96" aria-label="Star">
          <polygon points="48,8 58,38 90,38 64,57 74,88 48,69 22,88 32,57 6,38 38,38" fill="var(--star)"/>
        </svg>
      </div>
    </div>
    <div class="menu-item" style="left:1000px; top:95px">
      <div class="menu-item__label">Friend of tovami</div>
      <div class="tile" style="margin-top:17px">
        <svg viewBox="0 0 96 96" aria-label="Plus">
          <path d="M37 6 H59 V37 H90 V59 H59 V90 H37 V59 H6 V37 H37 Z" fill="var(--icon-dark)" stroke="var(--icon-dark)" stroke-width="4" stroke-linejoin="round"/>
        </svg>
      </div>
    </div>

    <div class="menu-item" style="left:194px; top:362px">
      <div class="menu-item__label">Map view</div>
      <div class="tile" style="margin-top:9px"><div class="icon-fill icon-fill--globe" role="img" aria-label="Globe map icon"></div></div>
    </div>
    <div class="menu-item" style="left:382px; top:367px">
      <div class="menu-item__label">Contractual issue</div>
      <div class="tile" style="margin-top:6px"><div class="icon-fill icon-fill--papers" role="img" aria-label="Signed contract documents icon"></div></div>
    </div>
    <div class="menu-item" style="left:582px; top:367px">
      <div class="menu-item__label">Target consumer</div>
      <div class="tile" style="margin-top:6px">
        <svg viewBox="0 0 96 96" aria-label="Target">
          <circle cx="48" cy="48" r="44" fill="var(--target)"/><circle cx="48" cy="48" r="35" fill="#fff"/>
          <circle cx="48" cy="48" r="26" fill="var(--target)"/><circle cx="48" cy="48" r="17" fill="#fff"/>
          <circle cx="48" cy="48" r="9" fill="var(--target)"/>
        </svg>
      </div>
    </div>
    <div class="menu-item" style="left:790px; top:367px">
      <div class="menu-item__label">Category of a place</div>
      <div class="tile" style="margin-top:6px">
        <svg viewBox="0 0 96 96" aria-label="Folder">
          <rect x="34" y="14" width="22" height="10" rx="2" fill="#555"/><rect x="62" y="14" width="22" height="10" rx="2" fill="#555"/>
          <path d="M6 16 H30 V26 H88 V84 H6 Z" fill="var(--icon-grey)"/>
        </svg>
      </div>
    </div>
    <div class="menu-item" style="left:1000px; top:361px">
      <div class="menu-item__label">Ambient place</div>
      <div class="tile" style="margin-top:15px"><div class="icon-fill icon-fill--chair" role="img" aria-label="Armchair icon"></div></div>
    </div>
  </nav>

  <div class="action action--primary"><span class="action__arrow"></span><span class="action__text">Menu selector</span></div>
  <div class="action action--secondary"><span class="action__arrow"></span><span class="action__text">Cerca</span></div>
</body>
</html>
```